indépendant en tant que Massothérapeute et Préparateur Mental, j'ai besoin de ...

Massothérapeute et préparateur mental indépendant, je recherche une carte de visite sobre et dynamique, sans images liées au massage ou à la préparation mentale mais intégrant mon logo. Les couleurs que j'aime bien sont : Blanc, gris, anthracite, noir et jaune

Contact Information for Business Card

carte de préférence Horizontale
neutre qui puisse toucher le deux domaines Massothérapie et préparation mentale

Requirements
Must have
• mon projet doit intégrer au recto:
LOGO
Loïc Vermande
078 315 26 49
info@loicvermande-exemple.ch
et éventuellement www.loicvermande-exemple.ch

et au verso les deux adresses:

Chemin des Ormelets 27B
1400 Yverdon-les-Bains

Rue des Tanneries 9
1700 Fribourg

Should not have
• mon projet ne doit pas contenir d'image en liens avec le massage ni la préparation mentale.

```html
<!DOCTYPE html>
<html lang="fr">
<head>
<meta charset="utf-8">
<title>Loïc Vermande – Cartes de visite</title>
<link rel="stylesheet" href="https://fonts.googleapis.com/css2?family=Lato:wght@400;700&display=swap">
<style>
  :root {
    --backdrop: #e4e3e1;
    --card-black: #050505;
    --card-white: #ffffff;
    --ink: #1b1b1b;
    --ink-soft: #6e6e6e;
    --rule: #555555;
    --on-dark: #ffffff;
  }
  * { box-sizing: border-box; margin: 0; padding: 0; }
  html, body { width: 1200px; height: 847px; overflow: hidden; }
  body {
    background: var(--backdrop);
    font-family: "Lato", sans-serif;
    position: relative;
  }
  .card {
    position: absolute;
    top: 268px;
    width: 540px;
    height: 310px;
    box-shadow: 0 10px 28px rgba(0,0,0,.22);
  }
  .card--front { left: 40px; background: var(--card-black); }
  .card--back  { left: 620px; background: var(--card-white); color: var(--ink); }

  /* brand lockup */
  .brand { display: flex; align-items: center; gap: 12px; }
  .brand__dot { width: 34px; height: 34px; border-radius: 50%; flex: none; }
  .brand__text { display: flex; flex-direction: column; }
  .brand__name { font-weight: 700; letter-spacing: .02em; line-height: 1; }
  .brand__tagline {
    font-size: 9px; text-transform: uppercase; letter-spacing: .08em;
    margin-top: 4px; font-weight: 400;
  }

  .card--front .brand {
    position: absolute; left: 50%; top: 50%;
    transform: translate(-50%, -50%);
    color: var(--on-dark);
  }
  .card--front .brand__dot { background: var(--on-dark); width: 40px; height: 40px; }
  .card--front .brand__name { font-size: 26px; }
  .card--front .brand__tagline { font-size: 10px; }

  .card--back .brand { position: absolute; right: 32px; top: 30px; color: var(--ink); }
  .card--back .brand__dot { background: var(--ink); }
  .card--back .brand__name { font-size: 20px; }

  .person { position: absolute; left: 34px; top: 78px; }
  .person__name { font-size: 22px; font-weight: 700; }
  .person__role { font-size: 13px; color: var(--ink-soft); margin-top: 2px; }

  .divider {
    position: absolute; left: 34px; right: 32px; top: 150px;
    border-top: 1px solid var(--rule);
  }

  .contacts {
    position: absolute; left: 34px; top: 168px;
    list-style: none; font-size: 13px; color: var(--ink-soft);
  }
  .contacts li { display: flex; align-items: center; gap: 10px; height: 22px; }
  .contacts svg { width: 13px; height: 13px; fill: var(--ink); flex: none; }

  .address {
    position: absolute; right: 32px; text-align: right;
    font-size: 14px; color: var(--ink-soft); line-height: 1.4;
    font-style: normal;
  }
  .address--fribourg { top: 100px; }
  .address--yverdon { top: 230px; }
</style>
</head>
<body>

<section class="card card--front" aria-label="Recto">
  <div class="brand">
    <span class="brand__dot"></span>
    <div class="brand__text">
      <span class="brand__name">Loïc Vermande</span>
      <span class="brand__tagline">Massothérapeute / Préparateur mental</span>
    </div>
  </div>
</section>

<section class="card card--back" aria-label="Verso">
  <div class="brand">
    <span class="brand__dot"></span>
    <div class="brand__text">
      <span class="brand__name">Loïc Vermande</span>
      <span class="brand__tagline">Massothérapeute / Préparateur mental</span>
    </div>
  </div>

  <div class="person">
    <p class="person__name">Loïc Vermande</p>
    <p class="person__role">Founder &amp; CEO</p>
  </div>

  <address class="address address--fribourg">Rue des Tanneries 9<br>1700 Fribourg</address>

  <div class="divider"></div>

  <ul class="contacts">
    <li>
      <svg viewBox="0 0 24 24" aria-hidden="true"><path d="M6.6 10.8a15.1 15.1 0 0 0 6.6 6.6l2.2-2.2c.3-.3.7-.4 1-.2 1.1.4 2.3.6 3.6.6.6 0 1 .4 1 1V20c0 .6-.4 1-1 1A17 17 0 0 1 3 4c0-.6.4-1 1-1h3.5c.6 0 1 .4 1 1 0 1.3.2 2.5.6 3.6.1.3 0 .7-.2 1z"/></svg>
      078 315 26 49
    </li>
    <li>
      <svg viewBox="0 0 24 24" aria-hidden="true"><path d="M2 5h20v14H2zm2 2v.5l8 5 8-5V7zm0 2.8V17h16V9.8l-8 5z"/></svg>
      info@loicvermande-exemple.ch
    </li>
    <li>
      <svg viewBox="0 0 24 24" aria-hidden="true"><path d="M12 2a10 10 0 1 0 0 20 10 10 0 0 0 0-20zm6.9 9h-3c-.1-2.4-.6-4.5-1.4-6A8 8 0 0 1 18.9 11zM12 4c.9 1.2 1.7 3.6 1.9 7h-3.8C10.3 7.6 11.1 5.2 12 4zM9.5 5c-.8 1.5-1.3 3.6-1.4 6h-3A8 8 0 0 1 9.5 5zM5.1 13h3c.1 2.4.6 4.5 1.4 6A8 8 0 0 1 5.1 13zm6.9 7c-.9-1.2-1.7-3.6-1.9-7h3.8c-.2 3.4-1 5.8-1.9 7zm2.5-1c.8-1.5 1.3-3.6 1.4-6h3a8 8 0 0 1-4.4 6z"/></svg>
      www.loicvermande-exemple.ch
    </li>
  </ul>

  <address class="address address--yverdon">Chemin des Ormelets 27B<br>1400 Yverdon-les-Bains</address>
</section>

</body>
</html>
```